Business Card Design Project

Business Card
We are rebranding with a new logo
Industry/Entity Type
Business
Contact Information for Business Card
Doug Farrow +61 457820913 doug@lumora.com.au P.O. Box 728 Kelmscott QLD 4309
Requirements
Must have
- Logo

```html
<!DOCTYPE html>
<html lang="en">
<head>
<meta charset="utf-8">
<title>Lumora Business Card</title>
<link rel="stylesheet" href="https://fonts.googleapis.com/css2?family=Roboto:wght@400;500&display=swap">
<style>
  :root {
    --bg: #2b2b2b;
    --blue-light: #1ea6dc;
    --blue-dark: #0b6f98;
    --orange: #f07d1e;
    --orange-dark: #b85a0f;
    --white: #ffffff;
    --ink: #1e1e1e;
  }
  * { box-sizing: border-box; margin: 0; padding: 0; }
  html, body { width: 1200px; height: 900px; overflow: hidden; }
  body {
    background: var(--bg);
    font-family: "Roboto", Arial, sans-serif;
    position: relative;
  }
  .card {
    position: absolute;
    top: 290px;
    width: 560px;
    height: 320px;
    border-radius: 18px;
    overflow: hidden;
    box-shadow: 0 10px 30px rgba(0,0,0,.5);
  }
  .card-front {
    left: 30px;
    background: linear-gradient(160deg, var(--blue-light), var(--blue-dark));
    display: flex;
    align-items: center;
    justify-content: center;
  }
  .brand {
    display: flex;
    align-items: center;
    gap: 16px;
    font-weight: 500;
    font-size: 64px;
    letter-spacing: 1px;
  }
  .brand-dot {
    width: 40px; height: 40px; border-radius: 50%;
  }
  .card-front .brand { color: var(--white); }
  .card-front .brand-dot { background: var(--orange); }

  .card-back {
    left: 610px;
    background: var(--white);
  }
  .back-panel {
    position: absolute;
    left: 250px; top: 0; right: 0; bottom: 0;
    background: linear-gradient(160deg, var(--blue-light), var(--blue-dark));
    box-shadow: -6px 0 14px rgba(0,0,0,.25);
  }
  .name-ribbon {
    position: absolute;
    left: 225px; top: 34px;
    width: 310px; height: 52px;
    background: var(--orange);
    color: var(--white);
    font-size: 26px;
    display: flex; align-items: center;
    padding-left: 36px;
  }
  .ribbon-fold {
    position: absolute;
    left: 225px; top: 86px;
    width: 0; height: 0;
    border-top: 18px solid var(--orange-dark);
    border-left: 25px solid transparent;
  }
  .card-back .brand {
    position: absolute;
    left: 40px; top: 95px;
    color: var(--blue-light);
    font-size: 48px;
    gap: 12px;
  }
  .card-back .brand-dot { background: var(--orange); width: 30px; height: 30px; }
  .contacts {
    position: absolute;
    left: 44px; bottom: 36px;
    list-style: none;
    color: var(--ink);
    font-size: 15px;
  }
  .contacts li { display: flex; align-items: center; gap: 12px; margin-top: 8px; }
  .icon {
    width: 24px; height: 24px;
    background: var(--blue-dark);
    display: flex; align-items: center; justify-content: center;
  }
  .address {
    position: absolute;
    right: 34px; bottom: 36px;
    color: var(--white);
    font-size: 14px;
    line-height: 1.4;
    text-align: right;
  }
</style>
</head>
<body>
  <section class="card card-front">
    <div class="brand"><span class="brand-dot"></span>Lumora</div>
  </section>

  <section class="card card-back">
    <div class="back-panel"></div>
    <div class="name-ribbon">Doug Farrow</div>
    <div class="ribbon-fold"></div>
    <div class="brand"><span class="brand-dot"></span>Lumora</div>
    <ul class="contacts">
      <li>
        <span class="icon">
          <svg width="14" height="14" viewBox="0 0 24 24"><path fill="#fff" d="M6.6 10.8a15.1 15.1 0 0 0 6.6 6.6l2.2-2.2c.3-.3.7-.4 1-.2 1.1.4 2.3.6 3.6.6.6 0 1 .4 1 1V20c0 .6-.4 1-1 1A17 17 0 0 1 3 4c0-.6.4-1 1-1h3.5c.6 0 1 .4 1 1 0 1.3.2 2.5.6 3.6.1.3 0 .7-.2 1z"/></svg>
        </span>+61 457820913
      </li>
      <li>
        <span class="icon">
          <svg width="14" height="12" viewBox="0 0 24 18"><rect x="1" y="1" width="22" height="16" fill="none" stroke="#fff" stroke-width="2"/><path d="M1 1l11 9 11-9" fill="none" stroke="#fff" stroke-width="2"/></svg>
        </span>doug@lumora.com.au
      </li>
    </ul>
    <p class="address">P.O. Box 728<br>Kelmscott QLD 4309</p>
  </section>
</body>
</html>
```